App Design for FlavorRoam

We need an app design for a new app called FlavorRoam, which is an app designed to inspire exploration through personalized recipe generation, local restaurant discoveries, and a vibrant community platform. It caters to food enthusiasts looking to explore global cuisines or find the best local dining spots, offering a premium experience with selected features available for free.

-------UPDATED-----
This app will be AI Driven and may not be heavily dependent on media (images,videos) at first, especially for the Recipe generator feature. Our goal is to still have attractive UI. The core functionalities we are looking are the following
1. Recipe Generator: Either user choose a specific cuisine(italian,spanish), or user inputs ingredients and get recipe, or get recipe for different occasions (xmas, thanksgiving ) and get a randomly get recipe to cook, plain simple. We expect the recipes to be displayed in clear and not too generic manner starting with ingredients and expected duration at top and then step by step guide. We also intend to enable premium users to have playful action button or icon to get unlimited recipes generated until they find what they like and also have save for later feature. These premium features should be disabled for free users and prompted to subscribe if they click them with nice popup
2. Restaurant Recommendation - will have selected pictures and will be based on inputs such as zip code and other filters such as cousine types. Premium users can filter by price range, get unlimited recommendation, see actual price range in the recommendation and can save for later where they can find it later. Free users cannot filter by price (disabled) and should see it hidden in the recommendation
3. Meal Planning - will include just simple and random meal plan with just one button or limited interaction for free, users need to subscribe to get features such as customized plan such as considering allergies or diet preferences. Premium users can also get a shopping checklist of ingredients for weekly meal preps and their step by step guide for each meal recipe.
2. Community Sharing: users can view posts and engage with community content
Updates

Hello Designers,

The initial price was not fair for the work. So I have increased it. There will also be $50-100 bonus for those who come up with great designs or for those who incorporate interesting stuff. Thank you! Much appreciated 🙏

Colors
0054AA
0677BA
7BADD7
CADEEF
E8F1F8
0094D4
00A9DD
6FCCEA
C7EBF8
E9F6FB
00AB8E
00BBA5
67D7C9
C6EFE9
E9F9F6
FFC000
F8CF3A
FAE287
FDF2CF
FEFAEE
F0912C
F2A743
F7CA91
FBE8D2
FDF5EE
EE7325
F08F49
F5BC92
FAE3D3
FDF4ED
A7469A
B969AE
D3A5CF
EDDBEB
F8F0F9
6B429C
8869AF
B7A5CE
E3DAEB
F3F0F8

```html
<!DOCTYPE html>
<html lang="en">
<head>
<meta charset="utf-8">
<title>FlavorRoam — Restaurant Recommendation &amp; Meal Planning</title>
<link rel="stylesheet" href="https://fonts.googleapis.com/css2?family=Poppins:wght@400;500;600&display=swap">
<style>
:root{
  --blue-900:#0054AA;
  --blue-700:#0677BA;
  --sky:#0094D4;
  --sky-2:#00A9DD;
  --sky-soft:#E9F6FB;
  --ink:#1F2125;
  --text:#3A3D42;
  --muted:#7A7F87;
  --line:#E4E7EC;
  --surface:#FFFFFF;
  --canvas:#F3F5F8;
  --field:#F4F6F9;
  --disabled:#D6DADF;
  --icon-grey:#B4B9C0;
}
*{box-sizing:border-box;margin:0;padding:0}
html,body{width:1200px;height:776px;overflow:hidden;background:#fff}
body{font-family:"Poppins",sans-serif;color:var(--ink)}
.board{position:absolute;left:0;top:0;width:2400px;height:1552px;transform:scale(.5);transform-origin:0 0}
.section-title{position:absolute;top:48px;font-size:30px;font-weight:600;letter-spacing:-.2px;color:var(--ink)}

.screen{position:absolute;top:115px;width:256px;border-radius:34px;background:var(--canvas);overflow:hidden;border:1px solid var(--line)}
.screen-top{background:var(--surface);padding-bottom:12px;border-radius:0 0 16px 16px}
.status-bar{height:36px;display:flex;align-items:center;justify-content:space-between;padding:0 22px 0 40px;font-size:11px;font-weight:600}
.status-icons{display:flex;gap:3px;align-items:center}
.app-header{min-height:32px;display:flex;align-items:center;gap:10px;padding:0 14px 0 14px}
.app-header .title{flex:1;font-size:14.5px;font-weight:500;line-height:22px}
.app-header.two-line{align-items:flex-start}
.app-header.two-line .hdr-icon{margin-top:3px}
.hdr-icon{width:16px;height:16px;color:var(--icon-grey)}
.avatar{width:28px;height:28px;border-radius:50%;background:radial-gradient(circle at 50% 35%,#3d6f72 0,#25494d 60%,#1a3336 100%);border:2px solid #fff;box-shadow:0 0 0 1px var(--line)}

.search{margin:19px 14px 0;height:32px;border:1px solid var(--line);border-radius:16px;display:flex;align-items:center;justify-content:space-between;padding:0 6px 0 12px;font-size:10.5px;color:#BFC3C9}
.search.filled{color:var(--ink)}
.round-ico{width:20px;height:20px;border-radius:50%;background:var(--field);display:flex;align-items:center;justify-content:center;color:var(--icon-grey)}

.tabs{display:flex;justify-content:space-around;padding:0 4px;margin-top:14px}
.tabs.three{justify-content:space-around;padding:0 14px}
.tab{width:56px;text-align:center;font-size:7.5px;color:var(--icon-grey)}
.tab-ico{position:relative;width:28px;height:28px;border-radius:50%;background:#EFF1F4;margin:0 auto 4px;display:flex;align-items:center;justify-content:center;color:#C2C6CC}
.tab.active{color:var(--blue-900);font-weight:500}
.tab.active .tab-ico{background:var(--blue-900);color:#fff}
.pro-badge{position:absolute;top:-4px;right:-8px;width:12px;height:12px;border-radius:50%;background:var(--sky);border:1.5px solid #fff;display:flex;align-items:center;justify-content:center;color:#fff}

.card{background:var(--surface);margin:15px 14px 0;border-radius:14px;padding:12px}
.card-title{font-size:12px;font-weight:500;margin-bottom:12px}
.chips{display:grid;grid-template-columns:repeat(3,1fr);gap:6px}
.chip{height:26px;border:1px solid var(--line);border-radius:13px;font-size:9.5px;display:flex;align-items:center;justify-content:center;color:var(--text)}
.chip.selected{background:var(--blue-900);border-color:var(--blue-900);color:#fff}
.link{display:block;text-align:center;color:var(--blue-700);font-size:9px;font-weight:500;margin-top:12px}

.primary-btn{display:flex;align-items:center;justify-content:center;margin:20px auto 0;height:32px;border-radius:16px;background:var(--sky);color:#fff;font-size:10.5px;font-weight:500;padding:0 16px;width:max-content}
.btn-pair{display:flex;gap:10px;margin:20px 14px 0}
.ghost-btn{position:relative;flex:1;height:32px;border-radius:16px;background:var(--disabled);color:#fff;font-size:10px;display:flex;align-items:center;justify-content:center}
.ghost-btn .pro-badge{top:-6px;right:2px}

.upgrade-bar{position:absolute;left:0;right:0;bottom:0;height:72px;background:var(--surface);border-top:1px solid var(--line);padding:10px 14px 0;display:flex;align-items:flex-start;justify-content:space-between}
.upgrade-bar p{font-size:9.5px;line-height:14px;color:var(--muted)}
.upgrade-btn{height:26px;border:1px solid var(--sky);border-radius:13px;display:flex;align-items:center;gap:5px;padding:0 10px;font-size:10px;font-weight:500;color:var(--blue-700);margin-top:2px}
.home-indicator{position:absolute;left:50%;bottom:8px;width:88px;height:3px;margin-left:-44px;border-radius:2px;background:var(--ink)}

.intro{font-size:10.5px;line-height:16px;color:var(--text);padding:18px 14px 0}
.hero-photo{margin:12px 14px 0;height:120px;border-radius:10px}
.photo-restaurant{background:linear-gradient(135deg,#5a1e24 0%,#a7373f 35%,#3a2a26 65%,#1b1714 100%)}
.photo-meal{background:radial-gradient(ellipse at 55% 55%,#c2451f 0%,#8a2a14 35%,#1f4c8c 62%,#173660 100%)}
.place-name{font-size:17px;font-weight:600;padding:14px 14px 0}
.address{font-size:10px;line-height:16px;color:var(--text);padding:8px 14px 0}
.meta{display:flex;align-items:center;gap:6px;font-size:9.5px;color:var(--muted);padding:0 14px;margin-top:8px}
.meta b{font-weight:500;color:var(--ink)}
.meta svg{color:var(--icon-grey)}

.field-label{font-size:10.5px;color:var(--text);padding:13px 14px 0}
.segments{display:flex;gap:6px;padding:10px 14px 0}
.segment{flex:1;height:30px;border:1px solid var(--line);border-radius:15px;font-size:9.5px;display:flex;align-items:center;justify-content:center;color:var(--text)}
.segment.selected{background:var(--blue-900);border-color:var(--blue-900);color:#fff}
.divider{height:1px;background:var(--line);margin:12px 0 0}

.toggle-row{display:flex;align-items:center;justify-content:space-between;font-size:11.5px;font-weight:500}
.toggle{width:26px;height:15px;border-radius:8px;background:#DADDE2;position:relative}
.toggle::after{content:"";position:absolute;left:2px;top:2px;width:11px;height:11px;border-radius:50%;background:#fff}
.toggle.on{background:var(--blue-900)}
.toggle.on::after{left:13px}
.ingredient-input{margin-top:10px;height:32px;border:1px solid var(--line);border-radius:16px;display:flex;align-items:center;justify-content:space-between;padding:0 6px 0 12px;font-size:10.5px;color:#BFC3C9}
.ingredient-row{margin-top:6px;height:26px;background:var(--field);border-radius:8px;display:flex;align-items:center;justify-content:space-between;padding:0 10px;font-size:10.5px;color:var(--text)}
.ingredient-row .qty{font-size:10px;color:var(--ink)}
.ingredient-row .qty small{font-size:9px;color:var(--muted)}
.ingredient-row.removable{background:var(--surface);border:1px solid var(--line);border-radius:14px;height:28px}
.toggle-row + .ingredient-row{margin-top:14px}
.regen{display:flex;align-items:center;justify-content:center;gap:5px;color:var(--blue-700);font-size:9.5px;font-weight:500;margin-top:12px}

.prep-summary{text-align:center;padding-top:18px}
.prep-summary .lbl{font-size:10.5px;color:var(--text)}
.prep-summary .val{font-size:19px;font-weight:500;margin-top:2px}

.day{background:var(--surface);margin:14px 14px 0;border-radius:12px;padding:10px 12px;position:relative}
.day .day-num{font-size:9px;color:var(--text)}
.day .day-name{font-size:12px;font-weight:600;color:var(--blue-900);margin-top:2px}
.day .chev{position:absolute;right:12px;top:22px;color:var(--muted)}
.day-photo{height:105px;border-radius:8px;margin-top:14px}
.kv{display:flex;align-items:center;gap:5px;font-size:9.5px;color:var(--muted);margin-top:12px}
.kv + .kv{margin-top:8px}
.kv b{font-weight:500;color:var(--ink)}
.sub-title{font-size:10.5px;font-weight:600;margin-top:18px}
.list{list-style:none;margin-top:6px}
.list li{display:flex;justify-content:space-between;gap:8px;font-size:10px;line-height:14px;color:var(--text);padding:6px 0 5px 10px;position:relative}
.list li::before{content:"";position:absolute;left:0;top:12px;width:3px;height:3px;border-radius:50%;background:var(--icon-grey)}
.list li span:last-child{flex:none;color:var(--ink);font-size:9.5px}
.list li small{font-size:9px;color:var(--muted)}
.steps{list-style:none;margin-top:12px}
.steps li{display:flex;gap:10px;font-size:10.5px;line-height:16px;color:var(--text);margin-bottom:12px}
.steps li span:first-child{flex:none;width:9px}
</style>
</head>
<body>
<svg width="0" height="0" style="position:absolute" aria-hidden="true">
  <defs>
    <symbol id="i-home" viewBox="0 0 16 16"><path d="M2.5 7 8 2.5 13.5 7v6.5h-11z" fill="none" stroke="currentColor" stroke-width="1.3" stroke-linejoin="round"/><path d="M6.5 13.5v-3.5h3v3.5" fill="none" stroke="currentColor" stroke-width="1.3"/></symbol>
    <symbol id="i-back" viewBox="0 0 16 16"><path d="M14 8H2.5M7 3.5 2.5 8 7 12.5" fill="none" stroke="currentColor" stroke-width="1.3" stroke-linecap="round" stroke-linejoin="round"/></symbol>
    <symbol id="i-mic" viewBox="0 0 12 12"><rect x="4.2" y="1.2" width="3.6" height="6" rx="1.8" fill="none" stroke="currentColor" stroke-width="1"/><path d="M2.8 5.8a3.2 3.2 0 0 0 6.4 0M6 9v2" fill="none" stroke="currentColor" stroke-width="1"/></symbol>
    <symbol id="i-clear" viewBox="0 0 12 12"><circle cx="6" cy="6" r="4.8" fill="none" stroke="currentColor" stroke-width="1"/><path d="M4.2 4.2l3.6 3.6M7.8 4.2 4.2 7.8" stroke="currentColor" stroke-width="1"/></symbol>
    <symbol id="i-gem" viewBox="0 0 12 12"><path d="M3 1.8h6l2.2 2.8L6 10.5.8 4.6z" fill="none" stroke="currentColor" stroke-width="1.1" stroke-linejoin="round"/><path d="M.8 4.6h10.4M4.3 1.8 3.6 4.6 6 10.5l2.4-5.9-.7-2.8" fill="none" stroke="currentColor" stroke-width=".9"/></symbol>
    <symbol id="i-gem-solid" viewBox="0 0 12 12"><path d="M3 2h6l2 2.6L6 10 1 4.6z" fill="currentColor"/></symbol>
    <symbol id="i-hat" viewBox="0 0 16 16"><path d="M4.5 11.5V9A3 3 0 0 1 5.5 3.4a3 3 0 0 1 5 0A3 3 0 0 1 11.5 9v2.5z" fill="none" stroke="currentColor" stroke-width="1.3" stroke-linejoin="round"/><path d="M4.5 13.5h7" stroke="currentColor" stroke-width="1.3"/></symbol>
    <symbol id="i-party" viewBox="0 0 16 16"><path d="M3 13.5 6 5l5 5z" fill="none" stroke="currentColor" stroke-width="1.2" stroke-linejoin="round"/><path d="M9 3v1.5M12 4.5l-1 1M13 7.5h-1.5" stroke="currentColor" stroke-width="1.2" stroke-linecap="round"/></symbol>
    <symbol id="i-walk" viewBox="0 0 16 16"><circle cx="8.5" cy="3" r="1.3" fill="none" stroke="currentColor" stroke-width="1.1"/><path d="M8 5.5 6.5 9.5l2 1.5v3M6.5 9.5 5 14M8 5.5l2.5 2.5H12M8 5.5 5.5 7 5 9" fill="none" stroke="currentColor" stroke-width="1.1" stroke-linecap="round" stroke-linejoin="round"/></symbol>
    <symbol id="i-tag" viewBox="0 0 16 16"><path d="M8.5 2.5H13.5v5l-6 6-5-5z" fill="none" stroke="currentColor" stroke-width="1.2" stroke-linejoin="round"/><circle cx="11" cy="5" r="1" fill="currentColor"/></symbol>
    <symbol id="i-basket" viewBox="0 0 16 16"><rect x="2.5" y="6" width="11" height="7.5" rx="1.5" fill="none" stroke="currentColor" stroke-width="1.3"/><path d="M5 6V4a3 3 0 0 1 6 0v2M2.5 9.5h11M6 9.5v4M10 9.5v4" fill="none" stroke="currentColor" stroke-width="1.2"/></symbol>
    <symbol id="i-hand" viewBox="0 0 16 16"><path d="M5 8V4.5a1 1 0 0 1 2 0V7.5M7 7V3.5a1 1 0 0 1 2 0V7.5M9 7.5V4.5a1 1 0 0 1 2 0V9c0 3-1.8 4.5-4 4.5-1.8 0-2.8-1-3.6-2.5L2.3 8.8a1 1 0 0 1 1.7-1L5 9" fill="none" stroke="currentColor" stroke-width="1.1" stroke-linejoin="round"/></symbol>
    <symbol id="i-board" viewBox="0 0 16 16"><rect x="3" y="3" width="10" height="11" rx="1.5" fill="none" stroke="currentColor" stroke-width="1.2"/><path d="M6 2.5h4v2H6zM5.5 8h5M5.5 10.5h3" fill="none" stroke="currentColor" stroke-width="1.1"/></symbol>
    <symbol id="i-down" viewBox="0 0 12 12"><path d="M2.5 4.5 6 8l3.5-3.5" fill="none" stroke="currentColor" stroke-width="1.1" stroke-linecap="round" stroke-linejoin="round"/></symbol>
    <symbol id="i-up" viewBox="0 0 12 12"><path d="M2.5 7.5 6 4l3.5 3.5" fill="none" stroke="currentColor" stroke-width="1.1" stroke-linecap="round" stroke-linejoin="round"/></symbol>
    <symbol id="i-clock" viewBox="0 0 12 12"><circle cx="6" cy="6" r="4.6" fill="none" stroke="currentColor" stroke-width="1"/><path d="M6 3.5V6l1.8 1.2" fill="none" stroke="currentColor" stroke-width="1"/></symbol>
    <symbol id="i-refresh" viewBox="0 0 12 12"><path d="M2 5.5a4 4 0 0 1 7-2.3M10 6.5a4 4 0 0 1-7 2.3" fill="none" stroke="currentColor" stroke-width="1.1" stroke-linecap="round"/><path d="M9.3 1.5v2H7.3M2.7 10.5v-2h2" fill="none" stroke="currentColor" stroke-width="1.1" stroke-linecap="round" stroke-linejoin="round"/></symbol>
    <symbol id="i-status" viewBox="0 0 44 10"><rect x="0" y="6" width="2.2" height="3" rx=".5" fill="currentColor"/><rect x="3.2" y="4.5" width="2.2" height="4.5" rx=".5" fill="currentColor"/><rect x="6.4" y="3" width="2.2" height="6" rx=".5" fill="currentColor"/><rect x="9.6" y="1.2" width="2.2" height="7.8" rx=".5" fill="currentColor"/><path d="M15.5 4.2a6 6 0 0 1 8 0M17 5.8a3.8 3.8 0 0 1 5 0" fill="none" stroke="currentColor" stroke-width="1.2" stroke-linecap="round"/><circle cx="19.5" cy="8" r="1" fill="currentColor"/><rect x="27" y="1.2" width="14" height="7.6" rx="2" fill="none" stroke="currentColor" stroke-width=".9" opacity=".5"/><rect x="28.4" y="2.6" width="11.2" height="4.8" rx="1" fill="currentColor"/><rect x="41.6" y="3.6" width="1.4" height="2.8" rx=".6" fill="currentColor" opacity=".5"/></symbol>
  </defs>
</svg>

<main class="board">
  <h1 class="section-title" style="left:48px">3 of 4 : Restaurant Recommendation</h1>
  <h1 class="section-title" style="left:960px">4 of 4 : Meal Planning</h1>

  <!-- Restaurant: empty search -->
  <section class="screen" style="left:48px;height:555px">
    <div class="screen-top">
      <div class="status-bar"><span>9:41</span><svg class="status-icons" width="44" height="10"><use href="#i-status"/></svg></div>
      <header class="app-header"><svg class="hdr-icon"><use href="#i-home"/></svg><span class="title">Restaurant</span><span class="avatar"></span></header>
      <div class="search"><span>Enter ZIP code or city</span><span class="round-ico"><svg width="11" height="11"><use href="#i-mic"/></svg></span></div>
      <nav class="tabs">
        <div class="tab active"><div class="tab-ico"><svg width="16" height="16"><use href="#i-hat"/></svg></div>Cuisine</div>
        <div class="tab"><div class="tab-ico"><svg width="16" height="16"><use href="#i-party"/></svg></div>Occasion</div>
        <div class="tab"><div class="tab-ico"><svg width="16" height="16"><use href="#i-walk"/></svg><span class="pro-badge"><svg width="7" height="7"><use href="#i-gem-solid"/></svg></span></div>Distance</div>
        <div class="tab"><div class="tab-ico"><svg width="16" height="16"><use href="#i-tag"/></svg><span class="pro-badge"><svg width="7" height="7"><use href="#i-gem-solid"/></svg></span></div>Price</div>
      </nav>
    </div>
    <div class="card">
      <div class="card-title">Choose Cuisine</div>
      <div class="chips">
        <span class="chip">American</span><span class="chip">Italian</span><span class="chip">Mexican</span>
        <span class="chip">Japanese</span><span class="chip">Chinese</span><span class="chip">Indian</span>
        <span class="chip">English</span><span class="chip">French</span><span class="chip">Korean</span>
      </div>
      <span class="link">Load More</span>
    </div>
    <span class="primary-btn">Get a Place To Eat</span>
    <footer class="upgrade-bar"><p>Upgrade to premium and<br>enjoy the full features</p><span class="upgrade-btn"><svg width="11" height="11"><use href="#i-gem"/></svg>Upgrade</span><span class="home-indicator"></span></footer>
  </section>

  <!-- Restaurant: filled search -->
  <section class="screen" style="left:328px;height:555px">
    <div class="screen-top">
      <div class="status-bar"><span>9:41</span><svg class="status-icons" width="44" height="10"><use href="#i-status"/></svg></div>
      <header class="app-header"><svg class="hdr-icon"><use href="#i-home"/></svg><span class="title">Restaurant</span><span class="avatar"></span></header>
      <div class="search filled"><span>70000 - TX</span><span class="round-ico"><svg width="12" height="12"><use href="#i-clear"/></svg></span></div>
      <nav class="tabs">
        <div class="tab active"><div class="tab-ico"><svg width="16" height="16"><use href="#i-hat"/></svg></div>Cuisine</div>
        <div class="tab"><div class="tab-ico"><svg width="16" height="16"><use href="#i-party"/></svg></div>Occasion</div>
        <div class="tab"><div class="tab-ico"><svg width="16" height="16"><use href="#i-walk"/></svg><span class="pro-badge"><svg width="7" height="7"><use href="#i-gem-solid"/></svg></span></div>Distance</div>
        <div class="tab"><div class="tab-ico"><svg width="16" height="16"><use href="#i-tag"/></svg><span class="pro-badge"><svg width="7" height="7"><use href="#i-gem-solid"/></svg></span></div>Price</div>
      </nav>
    </div>
    <div class="card">
      <div class="card-title">Choose Cuisine</div>
      <div class="chips">
        <span class="chip">American</span><span class="chip">Italian</span><span class="chip">Mexican</span>
        <span class="chip">Japanese</span><span class="chip selected">Chinese</span><span class="chip">Indian</span>
        <span class="chip">English</span><span class="chip">French</span><span class="chip">Korean</span>
      </div>
      <span class="link">Load More</span>
    </div>
    <span class="primary-btn">Get a Place To Eat</span>
    <footer class="upgrade-bar"><p>Upgrade to premium and<br>enjoy the full features</p><span class="upgrade-btn"><svg width="11" height="11"><use href="#i-gem"/></svg>Upgrade</span><span class="home-indicator"></span></footer>
  </section>

  <!-- Recommended restaurant -->
  <section class="screen" style="left:608px;height:585px">
    <div class="screen-top" style="padding-bottom:16px">
      <div class="status-bar"><span>9:41</span><svg class="status-icons" width="44" height="10"><use href="#i-status"/></svg></div>
      <header class="app-header two-line"><svg class="hdr-icon"><use href="#i-back"/></svg><span class="title">Recommended<br>Restaurant</span><span class="avatar"></span></header>
      <p class="intro">Here's a good restaurant based on your preferences. A very nice food here.</p>
      <div class="hero-photo photo-restaurant" role="img" aria-label="Photo of the restaurant's dining room with red lanterns and wooden tables"></div>
      <h2 class="place-name">Golden Lantern Restaurant</h2>
      <p class="address">1840 Maple Ridge Rd #12, Lakeview, TX 70000, United States</p>
      <div class="meta" style="margin-top:14px"><svg width="12" height="12" viewBox="0 0 16 16"><use href="#i-hat"/></svg>Cuisine: <b>Chinese</b></div>
      <div class="meta" style="margin-top:12px"><svg width="12" height="12" viewBox="0 0 16 16"><use href="#i-walk"/></svg>Distance: <b>1.2 miles</b></div>
      <div class="meta" style="margin-top:12px"><svg width="12" height="12" viewBox="0 0 16 16"><use href="#i-tag"/></svg>Price range: <b>$7 ~ $85</b></div>
    </div>
    <div class="btn-pair">
      <span class="ghost-btn">Next<span class="pro-badge"><svg width="7" height="7"><use href="#i-gem-solid"/></svg></span></span>
      <span class="ghost-btn">Save For Later<span class="pro-badge"><svg width="7" height="7"><use href="#i-gem-solid"/></svg></span></span>
    </div>
    <footer class="upgrade-bar"><p>Upgrade to premium and<br>enjoy the full features</p><span class="upgrade-btn"><svg width="11" height="11"><use href="#i-gem"/></svg>Upgrade</span><span class="home-indicator"></span></footer>
  </section>

  <!-- Meal prep: empty -->
  <section class="screen" style="left:960px;height:555px">
    <div class="screen-top">
      <div class="status-bar"><span>9:41</span><svg class="status-icons" width="44" height="10"><use href="#i-status"/></svg></div>
      <header class="app-header"><svg class="hdr-icon"><use href="#i-home"/></svg><span class="title">Meal Prep</span><span class="avatar"></span></header>
      <p class="field-label">Choose meal prep duration:</p>
      <div class="segments"><span class="segment">2 days</span><span class="segment selected">3 days</span><span class="segment">5 days</span></div>
      <div class="divider"></div>
      <nav class="tabs three" style="margin-top:12px">
        <div class="tab active"><div class="tab-ico"><svg width="16" height="16"><use href="#i-basket"/></svg></div>Ingredients</div>
        <div class="tab"><div class="tab-ico"><svg width="16" height="16"><use href="#i-hand"/></svg><span class="pro-badge"><svg width="7" height="7"><use href="#i-gem-solid"/></svg></span></div>Allergies</div>
        <div class="tab"><div class="tab-ico"><svg width="16" height="16"><use href="#i-board"/></svg><span class="pro-badge"><svg width="7" height="7"><use href="#i-gem-solid"/></svg></span></div>Dietary</div>
      </nav>
    </div>
    <div class="card">
      <div class="toggle-row">Auto Generate Ingredients<span class="toggle"></span></div>
      <div class="ingredient-input" style="margin-top:14px"><span>Add ingredient</span><span class="round-ico"><svg width="11" height="11"><use href="#i-mic"/></svg></span></div>
    </div>
    <span class="primary-btn" style="margin-top:22px">Plan a Meal</span>
    <footer class="upgrade-bar"><p>Upgrade to premium and<br>enjoy the full features</p><span class="upgrade-btn"><svg width="11" height="11"><use href="#i-gem"/></svg>Upgrade</span><span class="home-indicator"></span></footer>
  </section>

  <!-- Meal prep: manual ingredients -->
  <section class="screen" style="left:1240px;height:555px">
    <div class="screen-top">
      <div class="status-bar"><span>9:41</span><svg class="status-icons" width="44" height="10"><use href="#i-status"/></svg></div>
      <header class="app-header"><svg class="hdr-icon"><use href="#i-home"/></svg><span class="title">Meal Prep</span><span class="avatar"></span></header>
      <p class="field-label">Choose meal prep duration:</p>
      <div class="segments"><span class="segment">2 days</span><span class="segment selected">3 days</span><span class="segment">5 days</span></div>
      <div class="divider"></div>
      <nav class="tabs three" style="margin-top:12px">
        <div class="tab active"><div class="tab-ico"><svg width="16" height="16"><use href="#i-basket"/></svg></div>Ingredients</div>
        <div class="tab"><div class="tab-ico"><svg width="16" height="16"><use href="#i-hand"/></svg><span class="pro-badge"><svg width="7" height="7"><use href="#i-gem-solid"/></svg></span></div>Allergies</div>
        <div class="tab"><div class="tab-ico"><svg width="16" height="16"><use href="#i-board"/></svg><span class="pro-badge"><svg width="7" height="7"><use href="#i-gem-solid"/></svg></span></div>Dietary</div>
      </nav>
    </div>
    <div class="card">
      <div class="toggle-row">Auto Generate Ingredients<span class="toggle"></span></div>
      <div class="ingredient-row removable">Beef<svg width="13" height="13" style="color:var(--icon-grey)"><use href="#i-clear"/></svg></div>
      <div class="ingredient-row removable" style="margin-top:4px">Chicken<svg width="13" height="13" style="color:var(--icon-grey)"><use href="#i-clear"/></svg></div>
      <div class="ingredient-input" style="margin-top:4px"><span>Add ingredient</span><span class="round-ico"><svg width="11" height="11"><use href="#i-mic"/></svg></span></div>
    </div>
    <span class="primary-btn" style="margin-top:22px">Plan a Meal</span>
    <footer class="upgrade-bar"><p>Upgrade to premium and<br>enjoy the full features</p><span class="upgrade-btn"><svg width="11" height="11"><use href="#i-gem"/></svg>Upgrade</span><span class="home-indicator"></span></footer>
  </section>

  <!-- Meal prep: auto generated -->
  <section class="screen" style="left:1520px;height:715px">
    <div class="screen-top">
      <div class="status-bar"><span>9:41</span><svg class="status-icons" width="44" height="10"><use href="#i-status"/></svg></div>
      <header class="app-header"><svg class="hdr-icon"><use href="#i-home"/></svg><span class="title">Meal Prep</span><span class="avatar"></span></header>
      <p class="field-label">Choose meal prep duration:</p>
      <div class="segments"><span class="segment">2 days</span><span class="segment selected">3 days</span><span class="segment">5 days</span></div>
      <div class="divider"></div>
      <nav class="tabs three" style="margin-top:12px">
        <div class="tab active"><div class="tab-ico"><svg width="16" height="16"><use href="#i-basket"/></svg></div>Ingredients</div>
        <div class="tab"><div class="tab-ico"><svg width="16" height="16"><use href="#i-hand"/></svg><span class="pro-badge"><svg width="7" height="7"><use href="#i-gem-solid"/></svg></span></div>Allergies</div>
        <div class="tab"><div class="tab-ico"><svg width="16" height="16"><use href="#i-board"/></svg><span class="pro-badge"><svg width="7" height="7"><use href="#i-gem-solid"/></svg></span></div>Dietary</div>
      </nav>
    </div>
    <div class="card">
      <div class="toggle-row">Auto Generate Ingredients<span class="toggle on"></span></div>
      <div class="ingredient-row">Beef<span class="qty">40 <small>oz</small></span></div>
      <div class="ingredient-row">Bell Pepper<span class="qty">5</span></div>
      <div class="ingredient-row">Onion<span class="qty">3</span></div>
      <div class="ingredient-row">Chicken<span class="qty">1</span></div>
      <div class="ingredient-row">Potato<span class="qty">4</span></div>
      <div class="ingredient-row">Tomato<span class="qty">4</span></div>
      <div class="ingredient-row">Vegetable Oil<span class="qty">2 <small>tsp</small></span></div>
      <div class="ingredient-row">Iceberg lettuce<span class="qty">3 <small>cups</small></span></div>
      <div class="regen"><svg width="11" height="11"><use href="#i-refresh"/></svg>Re-generate</div>
    </div>
    <span class="primary-btn" style="margin-top:22px">Plan a Meal</span>
    <footer class="upgrade-bar"><p>Upgrade to premium and<br>enjoy the full features</p><span class="upgrade-btn"><svg width="11" height="11"><use href="#i-gem"/></svg>Upgrade</span><span class="home-indicator"></span></footer>
  </section>

  <!-- Recommended meal prep: collapsed -->
  <section class="screen" style="left:1800px;height:555px">
    <div class="screen-top" style="padding-bottom:16px">
      <div class="status-bar"><span>9:41</span><svg class="status-icons" width="44" height="10"><use href="#i-status"/></svg></div>
      <header class="app-header two-line"><svg class="hdr-icon"><use href="#i-back"/></svg><span class="title">Recommended Meal<br>Prep</span><span class="avatar"></span></header>
      <div class="prep-summary"><div class="lbl">Prep duration:</div><div class="val">3 days</div></div>
    </div>
    <div class="day"><div class="day-num">Day 1</div><div class="day-name">Mexican Beef Stir-Fry</div><svg class="chev" width="12" height="12"><use href="#i-down"/></svg></div>
    <div class="day"><div class="day-num">Day 2</div><div class="day-name">American Roasted Chicken</div><svg class="chev" width="12" height="12"><use href="#i-down"/></svg></div>
    <div class="day"><div class="day-num">Day 3</div><div class="day-name">Chinese Pepper Beef</div><svg class="chev" width="12" height="12"><use href="#i-down"/></svg></div>
    <div class="btn-pair">
      <span class="ghost-btn">Get New!<span class="pro-badge"><svg width="7" height="7"><use href="#i-gem-solid"/></svg></span></span>
      <span class="ghost-btn">Save For Later<span class="pro-badge"><svg width="7" height="7"><use href="#i-gem-solid"/></svg></span></span>
    </div>
    <footer class="upgrade-bar"><p>Upgrade to premium and<br>enjoy the full features</p><span class="upgrade-btn"><svg width="11" height="11"><use href="#i-gem"/></svg>Upgrade</span><span class="home-indicator"></span></footer>
  </section>

  <!-- Recommended meal prep: expanded day -->
  <section class="screen" style="left:2080px;height:1377px">
    <div class="screen-top" style="padding-bottom:16px">
      <div class="status-bar"><span>9:41</span><svg class="status-icons" width="44" height="10"><use href="#i-status"/></svg></div>
      <header class="app-header two-line"><svg class="hdr-icon"><use href="#i-back"/></svg><span class="title">Recommended Meal<br>Prep</span><span class="avatar"></span></header>
      <div class="prep-summary"><div class="lbl">Prep duration:</div><div class="val">3 days</div></div>
    </div>
    <article class="day" style="padding-bottom:4px">
      <div class="day-num">Day 1</div><div class="day-name">Mexican Beef Stir-Fry</div><svg class="chev" width="12" height="12"><use href="#i-up"/></svg>
      <div class="day-photo photo-meal" role="img" aria-label="Photo of beef and pepper stir-fry served in a blue bowl"></div>
      <div class="kv"><svg width="11" height="11" viewBox="0 0 16 16"><use href="#i-hat"/></svg>Cuisine: <b>Mexican</b></div>
      <div class="kv"><svg width="11" height="11"><use href="#i-clock"/></svg>Ready in: <b>27 minutes</b></div>
      <div class="sub-title">Your Ingredients</div>
      <ul class="list">
        <li><span>Beef</span><span>16 <small>oz</small></span></li>
        <li><span>Onion, cut into thin wedges</span><span>1</span></li>
        <li><span>Bell pepper, cut into strips</span><span>1</span></li>
      </ul>
      <div class="sub-title" style="margin-top:12px">More Ingredients</div>
      <ul class="list">
        <li><span>Vegetable oil</span><span>1 <small>tsp</small></span></li>
        <li><span>Garlic clove, minced</span><span>1</span></li>
        <li><span>Ground cumin</span><span>1 <small>tsp</small></span></li>
        <li><span>Dried oregano</span><span>1 <small>tsp</small></span></li>
        <li><span>Jalapeno pepper, seeded and cut into strips</span><span>1-2</span></li>
        <li><span>Iceberg lettuce, shredded</span><span>3 <small>cups</small></span></li>
      </ul>
      <div class="sub-title" style="margin-top:14px">Directions</div>
      <ol class="steps">
        <li><span>1.</span><span>Trim excess fat from the beef; slice steak diagonally across the grain into 1/8 inch strips. Set aside.</span></li>
        <li><span>2.</span><span>Combine oil, garlic, cumin, and oregano; stir well. Heat half of oil mixture in a large nonstick skillet over medium-high heat for 2 minutes. Add onion, red pepper, and jalapeno pepper, and stir-fry 2 minutes, or until crisp-tender. Remove vegetables from the skillet; set aside, and keep warm.</span></li>
        <li><span>3.</span><span>Add remaining oil mixture to the skillet. Add the reserved beef strips, and stir-fry 2 minutes. Return vegetables to the skillet and stir-fry until thoroughly heated. Serve over lettuce, and garnish if desired.</span></li>
      </ol>
    </article>
    <div class="day"><div class="day-num">Day 2</div><div class="day-name">American Roasted Beef</div><svg class="chev" width="12" height="12"><use href="#i-down"/></svg></div>
    <div class="day"><div class="day-num">Day 3</div><div class="day-name">Chinese Pepper Beef</div><svg class="chev" width="12" height="12"><use href="#i-down"/></svg></div>
    <div class="btn-pair">
      <span class="ghost-btn">Get New!<span class="pro-badge"><svg width="7" height="7"><use href="#i-gem-solid"/></svg></span></span>
      <span class="ghost-btn">Save For Later<span class="pro-badge"><svg width="7" height="7"><use href="#i-gem-solid"/></svg></span></span>
    </div>
    <footer class="upgrade-bar"><p>Upgrade to premium and<br>enjoy the full features</p><span class="upgrade-btn"><svg width="11" height="11"><use href="#i-gem"/></svg>Upgrade</span><span class="home-indicator"></span></footer>
  </section>
</main>
</body>
</html>
```